Meadowlark Learning Support Partners (MLSP)

This is a professional business card. Logo and picture are a must on the front of the card. I am an educational consultant. I have been consulting for the past three years for a company. I am now opening my own company. My goal for my consulting company is to eventually consult all over America.

Target Market(s)

Educators, schools, professionals

Industry/Entity Type

Consulting

Contact Information for Business Card

Picture/logo on front, simple modern design

Font styles to use
Serif

Colors
85abd2
0355a3
3176b5
cedeed

Requirements
Must have
• picture, logo,
• Dorotea Halvorsen, Ed.S
• address 5327 Quarry ridge Ln. Nashville, TN 37058
• Cell:616-555-0182
• Office: 629-555-0147
• www.Mlspwx.com
• halvorsendorotea@mailvexo.com

```html
<!DOCTYPE html>
<html lang="en">
<head>
<meta charset="utf-8">
<title>MLSP Business Card</title>
<link rel="stylesheet" href="https://fonts.googleapis.com/css2?family=Exo+2:wght@600;700&family=Lato:wght@400&display=swap">
<style>
  :root {
    --navy: #053a7c;
    --navy-deep: #0a3a7a;
    --mid-blue: #3176b5;
    --photo-top: #4f82c8;
    --photo-bottom: #2a4a78;
    --paper: #ffffff;
    --ink: #333333;
    --muted: #777777;
    --rule: #8a8a8a;
    --backdrop: #e8e6e3;
  }
  * { margin: 0; padding: 0; box-sizing: border-box; }
  html, body { width: 1200px; height: 848px; overflow: hidden; background: var(--backdrop); }
  .canvas { position: relative; width: 1200px; height: 848px; }

  .card { position: absolute; left: 262px; width: 654px; height: 354px; overflow: hidden;
          box-shadow: 0 6px 14px rgba(0,0,0,.25); }

  /* Front */
  .card-front { top: 46px; background: var(--navy); color: var(--paper); }
  .front-mark { position: absolute; left: 150px; top: 160px; width: 26px; height: 26px;
                border-radius: 50%; background: var(--paper); }
  .front-name { position: absolute; left: 190px; top: 150px; font-family: "Exo 2", sans-serif;
                font-weight: 700; font-size: 34px; letter-spacing: 4px; line-height: 44px; }
  .front-divider { position: absolute; left: 350px; top: 126px; width: 1px; height: 93px; background: var(--paper); }
  .front-fullname { position: absolute; left: 365px; top: 124px; font-family: "Exo 2", sans-serif;
                    font-weight: 700; font-size: 21px; line-height: 24.8px; letter-spacing: .5px; }
  .front-web { position: absolute; left: 0; right: 0; top: 314px; display: flex; align-items: center;
               justify-content: center; gap: 8px; font-family: "Lato", sans-serif; font-size: 14px; letter-spacing: 5px; }
  .front-web .rule { width: 70px; height: 1px; background: var(--paper); }

  /* Back */
  .card-back { top: 446px; background: var(--paper); }
  .back-mark { position: absolute; left: 95px; top: 60px; width: 44px; height: 44px;
               border-radius: 50%; background: var(--navy-deep); }
  .back-name { position: absolute; left: 43px; top: 118px; font-family: "Exo 2", sans-serif;
               font-weight: 700; font-size: 46px; letter-spacing: 3px; color: var(--navy-deep); line-height: 60px; }
  .portrait { position: absolute; left: 521px; top: 27px; width: 95px; height: 119px;
              background: linear-gradient(180deg, var(--photo-top), var(--photo-bottom)); }
  .person-name { position: absolute; right: 38px; top: 204px; font-family: "Exo 2", sans-serif;
                 font-weight: 700; font-size: 19px; color: var(--navy-deep); white-space: nowrap; }
  .person-rule { position: absolute; left: 0; top: 236px; width: 570px; height: 1px; background: var(--rule); }
  .person-role { position: absolute; right: 38px; top: 234px; font-family: "Lato", sans-serif;
                 font-size: 14px; color: var(--muted); }
  .side-tab { position: absolute; left: 646px; top: 209px; width: 8px; height: 32px; background: var(--navy-deep); }

  .contact-list { position: absolute; left: 43px; top: 260px; list-style: none;
                  font-family: "Lato", sans-serif; font-size: 15px; color: var(--ink); }
  .contact-list li { display: flex; align-items: center; gap: 6px; height: 18px; }
  .contact-list svg { width: 13px; height: 13px; fill: var(--navy-deep); flex: none; }

  .address { position: absolute; right: 38px; top: 298px; text-align: right; font-family: "Lato", sans-serif;
             font-size: 15px; line-height: 18px; color: var(--ink); }

  .footer-band { position: absolute; left: 0; bottom: 0; width: 654px; height: 12px; }
</style>
</head>
<body>
<div class="canvas">

  <section class="card card-front">
    <div class="front-mark"></div>
    <div class="front-name">MLSP</div>
    <div class="front-divider"></div>
    <div class="front-fullname">Meadowlark<br>Learning<br>Support<br>Partners</div>
    <div class="front-web"><span class="rule"></span>www.Mlspwx.com<span class="rule"></span></div>
  </section>

  <section class="card card-back">
    <div class="back-mark"></div>
    <div class="back-name">MLSP</div>
    <div class="portrait" role="img" aria-label="Portrait photo of Dorotea Halvorsen"></div>

    <div class="person-name">Dorotea Halvorsen, Ed.S</div>
    <div class="person-rule"></div>
    <div class="person-role">Owner</div>
    <div class="side-tab"></div>

    <ul class="contact-list">
      <li><svg viewBox="0 0 24 24"><path d="M6.6 10.8a15.1 15.1 0 0 0 6.6 6.6l2.2-2.2c.3-.3.7-.4 1-.2 1.1.4 2.3.6 3.6.6.6 0 1 .4 1 1V20c0 .6-.4 1-1 1A17 17 0 0 1 3 4c0-.6.4-1 1-1h3.5c.6 0 1 .4 1 1 0 1.3.2 2.5.6 3.6.1.3 0 .7-.2 1z"/></svg>629-555-0147</li>
      <li><svg viewBox="0 0 24 24"><path d="M7 1h10a2 2 0 0 1 2 2v18a2 2 0 0 1-2 2H7a2 2 0 0 1-2-2V3a2 2 0 0 1 2-2zm0 3v15h10V4z"/></svg>616-555-0182</li>
      <li><svg viewBox="0 0 24 24"><path d="M2 5h20v14H2zm2 2v.5l8 5 8-5V7l-8 5z"/></svg>halvorsendorotea@mailvexo.com</li>
      <li><svg viewBox="0 0 24 24"><path d="M12 2a10 10 0 1 0 0 20 10 10 0 0 0 0-20zm1 2.1c1.2 1.4 2 3.4 2.2 5.9H13zm-2 0V10H8.8c.2-2.5 1-4.5 2.2-5.9zM4.1 11H6.8c.1 1.2.3 2.3.7 3.3l-2.6.7A8 8 0 0 1 4.1 11zm4.7 1H11v6c-1.2-1.4-2-3.5-2.2-6zM13 12h2.2c-.2 2.5-1 4.6-2.2 6zm4.2-1h2.7a8 8 0 0 1-.8 4l-2.6-.7c.4-1 .6-2.1.7-3.3z"/></svg>www.Mlspwx.com</li>
    </ul>

    <div class="address">5327 Quarry ridge Ln.<br>Nashville, TN 37058</div>

    <svg class="footer-band" viewBox="0 0 654 12" preserveAspectRatio="none">
      <rect x="0" y="0" width="654" height="12" fill="var(--mid-blue)"/>
      <polygon points="0,0 292,0 284,12 0,12" fill="var(--navy-deep)"/>
      <polygon points="292,0 295,0 287,12 284,12" fill="var(--paper)"/>
    </svg>
  </section>

</div>
</body>
</html>
```